Double sided business Card voor Luchtkoel Brederwijk

Card design must be in line with our logo. Clean and professional look. Colors can be used, but not too wild.
Logo in frontside. Details on the backside. We want a qr in the design.

Details: (person)
name: Maarten Bosveld
tel: 06-48271935
maarten@luchtkoelbrederwijk.nl

tel: 088-5063918 (business general)
info@luchtkoelbrederwijk.nl

.

```html
<!DOCTYPE html>
<html lang="nl">
<head>
<meta charset="utf-8">
<title>Luchtkoel Brederwijk – visitekaartje</title>
<link rel="stylesheet" href="https://fonts.googleapis.com/css2?family=Roboto:wght@400;500&display=swap">
<style>
  :root {
    --backdrop: #6e6e6e;
    --card-dark: #1e1e1e;
    --card-light: #ffffff;
    --ink: #3c3c3c;
    --ink-soft: #555555;
    --brand-red: #e01b22;
    --brand-blue: #1f5fb0;
    --tint-red: #fbe6de;
    --tint-blue: #e6ebf7;
  }
  * { box-sizing: border-box; margin: 0; padding: 0; }
  html, body { width: 900px; height: 1200px; overflow: hidden; }
  body {
    background: var(--backdrop);
    font-family: "Roboto", sans-serif;
    position: relative;
  }
  .card {
    position: absolute;
    left: 147px;
    width: 606px;
    overflow: hidden;
  }
  .card--front { top: 200px; height: 386px; background: var(--card-dark); }
  .card--back  { top: 610px; height: 397px; background: var(--card-light); }

  .front-pattern {
    position: absolute; inset: 0;
    background: linear-gradient(100deg, #1b1b1b 0%, #262626 45%, #4a4a4a 100%);
  }
  .front-brand {
    position: absolute; left: 0; right: 0; top: 164px;
    text-align: center; color: #ffffff;
  }
  .front-brand .mark {
    display: block; width: 60px; height: 60px; margin: 0 auto 28px;
    border-radius: 50%; background: var(--brand-blue);
  }
  .front-brand .name-top {
    display: block; font-size: 32px; letter-spacing: 6px; line-height: 40px;
    text-transform: uppercase;
  }
  .front-brand .name-bottom {
    display: block; font-size: 42px; letter-spacing: 7px; line-height: 46px;
    text-transform: uppercase;
  }

  .back-decor {
    position: absolute; left: 307px; top: 215px; width: 301px; height: 182px;
    background: radial-gradient(ellipse at 60% 60%, var(--tint-blue) 0%, var(--tint-red) 55%, rgba(255,255,255,0) 80%);
    opacity: .8;
  }
  .back-brand {
    position: absolute; left: 26px; width: 220px; top: 71px;
    text-align: center; color: var(--ink);
  }
  .back-brand .mark {
    display: block; width: 56px; height: 56px; margin: 0 auto 22px;
    border-radius: 50%; background: var(--brand-blue);
  }
  .back-brand .name-top {
    display: block; font-size: 18px; letter-spacing: 3px; line-height: 22px;
    text-transform: uppercase;
  }
  .back-brand .name-bottom {
    display: block; font-size: 24px; letter-spacing: 4px; line-height: 30px;
    text-transform: uppercase;
  }

  .person { position: absolute; left: 290px; top: 57px; }
  .person .full-name { font-size: 26px; font-weight: 500; letter-spacing: .3px; }
  .person .first { color: var(--brand-red); }
  .person .last { color: var(--brand-blue); }
  .person .role { font-size: 16px; color: var(--ink-soft); margin-top: 2px; letter-spacing: .4px; }

  .contact-list { position: absolute; list-style: none; }
  .contact-list li {
    display: flex; align-items: center; gap: 6px;
    font-size: 16px; color: var(--ink); letter-spacing: .4px;
    height: 24px;
  }
  .contact-list .phone-number { letter-spacing: 2px; }
  .contact-list svg { width: 14px; height: 16px; flex: none; }
  .contact-list--personal { left: 290px; top: 149px; }
  .contact-list--general { left: 37px; top: 265px; }
</style>
</head>
<body>

<section class="card card--front">
  <div class="front-pattern" role="img" aria-label="Dark background with a repeating pattern of the brand symbol"></div>
  <div class="front-brand">
    <span class="mark"></span>
    <p class="name"><span class="name-top">Luchtkoel</span><span class="name-bottom">Brederwijk</span></p>
  </div>
</section>

<section class="card card--back">
  <div class="back-decor" role="img" aria-label="Large faint brand symbol in soft red and blue"></div>

  <div class="back-brand">
    <span class="mark"></span>
    <p class="name"><span class="name-top">Luchtkoel</span><span class="name-bottom">Brederwijk</span></p>
  </div>

  <div class="person">
    <p class="full-name"><span class="first">Maarten</span> <span class="last">Bosveld</span></p>
    <p class="role">Manager</p>
  </div>

  <ul class="contact-list contact-list--personal">
    <li>
      <svg viewBox="0 0 14 16" aria-hidden="true"><rect x="2.5" y="1" width="9" height="14" rx="1.5" fill="none" stroke="var(--brand-red)" stroke-width="1.8"/><circle cx="7" cy="12.3" r="1" fill="var(--brand-red)"/></svg>
      <span class="phone-number">06-48271935</span>
    </li>
    <li>
      <svg viewBox="0 0 14 16" aria-hidden="true"><rect x="0" y="3.5" width="14" height="9" fill="var(--brand-blue)"/><path d="M0 3.5 L7 8.5 L14 3.5" fill="none" stroke="#fff" stroke-width="1.2"/></svg>
      <span>maarten@luchtkoelbrederwijk.nl</span>
    </li>
  </ul>

  <ul class="contact-list contact-list--general">
    <li>
      <svg viewBox="0 0 14 16" aria-hidden="true"><rect x="2.5" y="1" width="9" height="14" rx="1.5" fill="none" stroke="var(--brand-red)" stroke-width="1.8"/><circle cx="7" cy="12.3" r="1" fill="var(--brand-red)"/></svg>
      <span class="phone-number">088-5063918</span>
    </li>
    <li>
      <svg viewBox="0 0 14 16" aria-hidden="true"><rect x="0" y="3.5" width="14" height="9" fill="var(--brand-blue)"/><path d="M0 3.5 L7 8.5 L14 3.5" fill="none" stroke="#fff" stroke-width="1.2"/></svg>
      <span>info@luchtkoelbrederwijk.nl</span>
    </li>
    <li>
      <svg viewBox="0 0 14 16" aria-hidden="true"><circle cx="7" cy="8" r="6.5" fill="var(--brand-red)"/><path d="M1 8 H13 M7 1.5 V14.5 M7 1.5 C3.5 5 3.5 11 7 14.5 M7 1.5 C10.5 5 10.5 11 7 14.5" fill="none" stroke="#fff" stroke-width=".9"/></svg>
      <span>www.luchtkoelbrederwijk.nl</span>
    </li>
  </ul>
</section>

</body>
</html>
```